Make Your Own Sushi Menu Design

We need to redesign our menu for both dine in and take away for our shop "Mr. Pebblo Sushi". Our sushi place differ to other sushi place because customer can choose what fillings they like inside their sushi and can choose their own toppings and sauce as well.

Not only that, we also offer a new take on sushi and seasonal sushi which depend on the seasonal ingredients therefore we need the menu to be easily interchangeable and to edit it.

At the moment we are using our original menu when we first started but since then we have expend our menu range. We need the menu to have MYO sushi page as well as preset sushi page. The theme or feel that we are looking for is a bit retro and industrial feel.

Target Market(s)

People age 18-50 Years old. Good lifestyle and young spirit

Industry/Entity Type

Industrial

Requirements
Must have
• MYO sushi page
Seasonal Sushi Page that is easy to change
Bento Menu
Should not have
• No food pictures.

```html
<!DOCTYPE html>
<html lang="en">
<head>
<meta charset="utf-8">
<title>Mr Pebblo Sushi – Menu</title>
<link href="https://fonts.googleapis.com/css2?family=Source+Sans+3:wght@400;600;700&display=swap" rel="stylesheet">
<style>
:root{
  --paper:#f4eee3;
  --paper-shade:#ebe3d4;
  --ink:#1c1b1a;
  --ink-soft:#3a3835;
  --maroon:#7e2b2b;
  --brick:#d2583a;
  --amber:#f3a428;
  --drink:#d8603c;
  --drink-panel:#f0d8cc;
  --leader:#8d8a85;
  --fold:#d8d1c4;
}
*{margin:0;padding:0;box-sizing:border-box}
html,body{width:1200px;height:848px;overflow:hidden}
body{font-family:"Source Sans 3",Arial,sans-serif;color:var(--ink);background:var(--paper)}
.menu{position:relative;width:1200px;height:848px;overflow:hidden;
  background:linear-gradient(160deg,var(--paper) 0%,var(--paper-shade) 55%,var(--paper) 100%)}
.fold{position:absolute;left:600px;top:0;width:1px;height:848px;background:var(--fold)}
.abs{position:absolute}
.section-title{position:absolute;font-size:27px;font-weight:400;color:var(--maroon);line-height:1}
.bar{position:absolute;height:11px}
.bar.brick{background:var(--brick)}
.bar.amber{background:var(--amber)}
.bar.maroon{background:var(--maroon)}
.bar.hatch{background:repeating-linear-gradient(120deg,#e9c3b4 0 2px,transparent 2px 5px)}
.bar.hatch.warm{background:repeating-linear-gradient(120deg,#f3d4a8 0 2px,transparent 2px 5px)}
.bar.hatch.cool{background:repeating-linear-gradient(120deg,#dcc2bc 0 2px,transparent 2px 5px)}

/* side dishes */
.item{position:absolute}
.item-name{font-size:15px;font-weight:700;line-height:19px;white-space:nowrap}
.item-desc{font-size:11px;line-height:15px;color:var(--ink-soft);margin-top:2px}
.item-desc .line{display:block;white-space:nowrap}
.price-line{display:flex;align-items:center;gap:8px;white-space:nowrap}
.price-line .text{flex:none}
.leader{flex:1;min-width:12px;height:1px;background:var(--leader)}
.gap{flex:1}
.price{font-size:15px;font-weight:700;flex:none}
.inline-row{display:flex;align-items:center;gap:8px}

.note{font-size:9px;color:var(--ink-soft)}

/* drinks */
.drinks-panel{position:absolute;left:28px;top:606px;width:540px;height:200px;border-radius:14px;background:var(--drink-panel);opacity:.75}
.drink{position:absolute;font-size:15.5px;color:var(--drink);line-height:1}
.drink-sub{position:absolute;font-size:12px;color:var(--ink);line-height:1.35}

/* rolls */
.roll{position:absolute}
.roll.col-a{left:620px;width:246px}
.roll.col-b{left:907px;width:256px}
.roll .item-name{font-size:14px;line-height:16px}
.roll .item-desc{font-size:12px;line-height:15.4px;color:var(--ink);margin-top:1px}
.roll .price{font-size:12px}
.roll .price-line{gap:6px}

/* seasonal slots */
.slot{position:absolute;width:260px}
.slot-name{font-size:13.5px;font-weight:700}
.slot-desc{font-size:11px;margin-top:5px;color:var(--ink-soft)}
.slot-price{position:relative;height:14px;margin-top:16px;font-size:11.5px;font-weight:700}
.slot-price .leader{position:absolute;left:60px;top:7px;width:75px}
.slot-price .s{position:absolute;left:141px}
.slot-price .l{position:absolute;left:187px}

.decor{position:absolute;left:830px;top:610px;width:260px;height:220px;border-radius:50%;
  background:radial-gradient(circle,rgba(150,145,135,.18) 0%,rgba(150,145,135,.08) 55%,transparent 72%)}
</style>
</head>
<body>
<main class="menu">
  <div class="fold"></div>

  <!-- SIDES -->
  <h2 class="section-title" style="left:28px;top:31px">Sides</h2>
  <div class="bar brick" style="left:105px;top:38px;width:110px"></div>
  <div class="bar hatch" style="left:222px;top:38px;width:330px"></div>

  <div class="item" style="left:28px;top:85px;width:242px">
    <div class="item-name">Mr Pebblo Special Sushi Salad</div>
    <div class="item-desc">
      <span class="line">Rocket Salad And a Combination Of Chopped</span>
      <span class="line">Fresh Salmon, Tuna, Steamed Prawn Served With</span>
      <span class="line">Cherry Tomatoes And Your Choice Of Dressing.</span>
      <span class="price-line" style="margin-top:2px"><span class="leader"></span><span class="price">$9.50</span></span>
    </div>
  </div>
  <div class="item" style="left:28px;top:179px;width:244px">
    <div class="item-name">Mr Pebblo Karaage</div>
    <div class="item-desc">
      <span class="line">Deep Fried Marinated Chicken Fillets Served</span>
      <span class="price-line"><span class="text">With Chilli Mayo.</span><span class="leader"></span><span class="price">$7.50</span></span>
    </div>
  </div>
  <div class="item" style="left:28px;top:250px;width:242px">
    <div class="item-name">New Style sashimi (Tuna/Salmon)</div>
    <div class="item-desc">
      <span class="line">Fresh tuna or salmon slices served with our</span>
      <span class="price-line"><span class="text">soya dressing.</span><span class="leader"></span><span class="price">$14.50</span></span>
    </div>
  </div>

  <div class="item" style="left:300px;top:84px;width:258px">
    <div class="item-name">Agedashi Tofu</div>
    <div class="item-desc">
      <span class="line">Lightly coated and fried fresh tofu in tempura</span>
      <span class="price-line"><span class="text">sauce.</span><span class="leader"></span><span class="price">$8.50</span></span>
    </div>
  </div>
  <div class="item" style="left:300px;top:145px;width:258px">
    <div class="item-name">Potato salad</div>
    <div class="item-desc">
      <span class="line">Japanese potato salad mixed with our chopped</span>
      <span class="price-line"><span class="text">karaage.</span><span class="leader"></span><span class="price">$6.50</span></span>
    </div>
  </div>
  <div class="item inline-row" style="left:298px;top:203px;width:260px"><span class="item-name">Japanese Seaweed Salad</span><span class="leader"></span><span class="price">$5.50</span></div>
  <div class="item inline-row" style="left:298px;top:229px;width:260px"><span class="item-name">Japanese Squid Salad</span><span class="leader"></span><span class="price">$5.50</span></div>
  <div class="item inline-row" style="left:298px;top:258px;width:260px"><span class="item-name">Teriyaki Chicken</span><span class="leader"></span><span class="price">$9.50</span></div>
  <div class="item inline-row" style="left:298px;top:285px;width:260px"><span class="item-name">Edamame</span><span class="leader"></span><span class="price">$6.00</span></div>

  <!-- BENTO -->
  <h2 class="section-title" style="left:28px;top:371px">Bento Box</h2>
  <p class="note abs" style="left:29px;top:404px">All comes with rice, salad and spring roll and karaage</p>
  <div class="item inline-row" style="left:28px;top:426px;width:244px"><span class="item-name">Teriyaki Chicken</span><span class="leader"></span><span class="price">$14.50</span></div>
  <div class="item inline-row" style="left:28px;top:452px;width:244px"><span class="item-name">Karaage(Crispy Chicken)</span><span class="leader"></span><span class="price">$14.50</span></div>
  <div class="item inline-row" style="left:28px;top:477px;width:244px"><span class="item-name">Teriyaki Tofu</span><span class="leader"></span><span class="price">$14.50</span></div>
  <div class="item inline-row" style="left:28px;top:503px;width:244px"><span class="item-name">Teriyaki Beef</span><span class="leader"></span><span class="price">$15.50</span></div>
  <div class="item inline-row" style="left:28px;top:529px;width:244px"><span class="item-name">Teriyaki Salmon</span><span class="leader"></span><span class="price">$15.50</span></div>

  <!-- ADDITIONAL / DESSERT -->
  <h2 class="section-title" style="left:294px;top:371px">Additional</h2>
  <div class="item inline-row" style="left:295px;top:410px;width:258px"><span class="item-name">Miso Soup</span><span class="leader"></span><span class="price">$2.50</span></div>
  <h2 class="section-title" style="left:294px;top:439px">Dessert</h2>
  <div class="item" style="left:296px;top:470px;width:256px">
    <div class="item-name">Mr Pebblo Cream Caramel</div>
    <div class="price-line"><span class="text" style="font-size:12px">Served With Black Sesame Ice Cream</span><span class="gap"></span><span class="price">$7.50</span></div>
  </div>
  <div class="item" style="left:294px;top:509px;width:258px">
    <div class="item-name">Lemon Green Tea Cheesecake</div>
    <div class="price-line"><span class="text" style="font-size:12px">Served With Seasonal Fruits</span><span class="leader"></span><span class="price">$8.50</span></div>
  </div>

  <!-- DRINKS -->
  <h2 class="section-title" style="left:38px;top:574px">Drinks</h2>
  <div class="drinks-panel"></div>
  <span class="drink" style="left:38px;top:616px">Mineral Water</span><span class="drink" style="left:250px;top:616px">$3.00</span>
  <span class="drink" style="left:38px;top:638px">Sparkling Water</span><span class="drink" style="left:250px;top:638px">$3.50</span>
  <span class="drink" style="left:38px;top:659px">Soft Drinks</span><span class="drink" style="left:250px;top:659px">$4.00</span>
  <span class="drink-sub" style="left:36px;top:683px">(Cola, Diet Cola, Cola Zero, Orange Fizz, Lemon Fizz)</span>
  <span class="drink" style="left:38px;top:701px">Brewleaf Iced Tea</span><span class="drink" style="left:250px;top:701px">$3.50</span>
  <span class="drink-sub" style="left:36px;top:717px;width:220px">(Lemon, Peach, Green Tea Lemon,<br>&nbsp;Green Tea Mango)</span>
  <span class="drink" style="left:38px;top:751px">Orchard Vale Juices</span><span class="drink" style="left:250px;top:751px">$4.00</span>
  <span class="drink-sub" style="left:36px;top:770px;width:230px">(Orange, Orange &amp; Mango, Pineapple,<br>&nbsp;5 Fruits, Apple)</span>

  <span class="drink" style="left:304px;top:616px">Lemon Lime Bitter</span><span class="drink" style="left:516px;top:616px">$3.50</span>
  <span class="drink" style="left:304px;top:637px">Ginger Beer</span><span class="drink" style="left:516px;top:637px">$3.50</span>
  <span class="drink" style="left:304px;top:658px">Calmira</span><span class="drink" style="left:516px;top:658px">$3.50</span>
  <span class="drink" style="left:304px;top:680px">Hanami Green Tea</span><span class="drink" style="left:516px;top:680px">$3.00</span>
  <span class="drink" style="left:304px;top:703px">Hot Green Tea (Refillable)</span><span class="drink" style="left:516px;top:703px">$2.50</span>

  <!-- SUSHI ROLLS -->
  <div class="bar amber" style="left:620px;top:38px;width:78px;height:13px"></div>
  <div class="bar hatch warm" style="left:704px;top:38px;width:236px;height:13px"></div>
  <h2 class="section-title" style="left:958px;top:31px">Sushi Rolls</h2>

  <div class="roll col-a" style="top:90px">
    <div class="item-name">Mr Pebblo Veggie Lover Roll</div>
    <div class="item-desc">
      <span class="line">Marinated enoki mushroom, avocado, roasted</span>
      <span class="line">capsicum, and miso eggplant with black sesame</span>
      <span class="price-line"><span class="text">sauce.</span><span class="leader"></span><span class="price">S/$8.00 L/ $13.50</span></span>
    </div>
  </div>
  <div class="roll col-a" style="top:155px">
    <div class="item-name">Cheesy Potato Roll</div>
    <div class="item-desc" style="margin-top:3px">
      <span class="line">Potato salad, cheese, sliced carrot and kanpyo</span>
      <span class="price-line"><span class="text">topped with frikake.</span><span class="gap"></span><span class="price">S/$8.00 L/$13.50</span></span>
    </div>
  </div>
  <div class="roll col-a" style="top:212px">
    <div class="item-name">South-East Roll</div>
    <div class="item-desc">
      <span class="line">Sliced carrots, coriander,avocado and egg,</span>
      <span class="line">topped with fried wonton skin served with</span>
      <span class="price-line"><span class="text">sweet and sour sauce.</span><span class="gap"></span><span class="price">S/$8.00 L/$13.50</span></span>
    </div>
  </div>
  <div class="roll col-a" style="top:283px">
    <div class="item-name">Katsu Kilpatrick Roll</div>
    <div class="item-desc">
      <span class="line">Choice of Chicken or Pork Katsu, with bacon,</span>
      <span class="line">cheese served with our BBQ and mustard sauce.</span>
      <span class="price-line"><span class="leader"></span><span class="price">S/$9.00 L/$15.50</span></span>
    </div>
  </div>
  <div class="roll col-a" style="top:353px">
    <div class="item-name">Crunchy Chicken Roll</div>
    <div class="item-desc" style="margin-top:4px">
      <span class="line">Chicken Katsu, iceberg lettuce and potato salad</span>
      <span class="line">topped with chilli mayo and fried shallots.</span>
      <span class="price-line"><span class="leader"></span><span class="price">S/$9.00 L/$15.50</span></span>
    </div>
  </div>
  <div class="roll col-a" style="top:426px">
    <div class="item-name">Chicken Lover Roll</div>
    <div class="item-desc" style="margin-top:3px">
      <span class="line">Grilled teriyaki Chicken, avocado, tamagoyaki</span>
      <span class="line">topped with mayonnaise, spring onion and</span>
      <span class="line">chopped karaage served with sliced lemon.</span>
      <span class="price-line"><span class="leader"></span><span class="price">S/$9.00 L/$15.50</span></span>
    </div>
  </div>
  <div class="roll col-a" style="top:511px">
    <div class="item-name">Spicy Tuna Roll</div>
    <div class="item-desc" style="margin-top:3px">
      <span class="line">Marinated fresh tuna and avocado topped with</span>
      <span class="price-line"><span class="text">tobikko and chilli mayo.</span><span class="gap"></span><span class="price">S/$9.00 L/$16.50</span></span>
    </div>
  </div>

  <div class="roll col-b" style="top:90px">
    <div class="item-name">Energy Roll</div>
    <div class="item-desc">
      <span class="line">Eel, chopped coriander and snow pea sprout</span>
      <span class="line">with our&nbsp; Sweet Teriyaki sauce.</span>
      <span class="price-line"><span class="gap"></span><span class="price">S/$10.00 L/$17.50</span></span>
    </div>
  </div>
  <div class="roll col-b" style="top:151px">
    <div class="item-name">Mr Pebblo Roll</div>
    <div class="item-desc">
      <span class="line">Tiger prawn fritters with crabsticks, sweet eggs</span>
      <span class="line">and avocado served with chilli mayo.</span>
      <span class="price-line" style="margin-top:2px"><span class="leader"></span><span class="price">S/$9.00 L/$15.50</span></span>
    </div>
  </div>
  <div class="roll col-b" style="top:216px">
    <div class="item-name">Crunchy Spider Roll</div>
    <div class="item-desc">
      <span class="line">Deep fried soft shell crab, iceberg lettuce,</span>
      <span class="line">cucumber topped with white sesame sauce</span>
      <span class="price-line"><span class="text">and shallots.</span><span class="leader"></span><span class="price">S/$9.00 L/$15.50</span></span>
    </div>
  </div>
  <div class="roll col-b" style="top:284px">
    <div class="item-name">Seafood Roll</div>
    <div class="item-desc">
      <span class="line">Fresh salmon slices, steamed prawn, cucumber</span>
      <span class="line">topped with fresh tuna flakes, chilli flakes, and</span>
      <span class="line">served with double sauce (wasabi aioli and</span>
      <span class="price-line"><span class="text">chilli mayo).</span><span class="leader"></span><span class="price">S/$10.50 L/$18.50</span></span>
    </div>
  </div>
  <div class="roll col-b" style="top:368px">
    <div class="item-name">Philadelphia Roll</div>
    <div class="item-desc">
      <span class="line">Smoked salmon, cream cheese topped with black</span>
      <span class="line">and white sesame seed with mayonnaise and our</span>
      <span class="price-line"><span class="text">sweet chilli sauce.</span><span class="leader"></span><span class="price">S/$9.00 L/$15.50</span></span>
    </div>
  </div>
  <div class="roll col-b" style="top:434px">
    <div class="item-name">Mexican Roll</div>
    <div class="item-desc">
      <span class="line">Grilled tenderloin, avocado, cheese, and roasted</span>
      <span class="line">capsicum, served with wasabi aioli and tomato</span>
      <span class="price-line"><span class="text">salsa.</span><span class="leader"></span><span class="price">S/$10.00 L/$17.50</span></span>
    </div>
  </div>
  <div class="roll col-b" style="top:501px;left:904px;width:259px">
    <div class="item-name">Surf &amp; Turf Roll</div>
    <div class="item-desc">
      <span class="line">Grilled steak rolled with steamed prawn and</span>
      <span class="line">snow pea sprout, topped with garlic chips and</span>
      <span class="line">chilli flakes, served with sweet onion sauce.</span>
      <span class="price-line"><span class="leader"></span><span class="price">S/$10.50 L/$18.50</span></span>
    </div>
  </div>

  <!-- SEASONAL -->
  <div class="decor" role="img" aria-label="Faint circular decorative pattern"></div>
  <h2 class="section-title" style="left:626px;top:589px">Seasonal Sushi</h2>
  <div class="bar maroon" style="left:856px;top:596px;width:78px;height:12px"></div>
  <div class="bar hatch cool" style="left:940px;top:596px;width:236px;height:12px"></div>

  <div class="slot" style="left:621px;top:628px"><div class="slot-name">Sushi Name</div><div class="slot-desc">Description</div><div class="slot-price"><span class="leader"></span><span class="s">S/$</span><span class="l">L/ $</span></div></div>
  <div class="slot" style="left:621px;top:697px"><div class="slot-name">Sushi Name</div><div class="slot-desc">Description</div><div class="slot-price"><span class="leader"></span><span class="s">S/$</span><span class="l">L/ $</span></div></div>
  <div class="slot" style="left:621px;top:766px"><div class="slot-name">Sushi Name</div><div class="slot-desc">Description</div><div class="slot-price"><span class="leader"></span><span class="s">S/$</span><span class="l">L/ $</span></div></div>
  <div class="slot" style="left:910px;top:627px"><div class="slot-name">Sushi Name</div><div class="slot-desc">Description</div><div class="slot-price"><span class="leader"></span><span class="s">S/$</span><span class="l">L/ $</span></div></div>
  <div class="slot" style="left:910px;top:696px"><div class="slot-name">Sushi Name</div><div class="slot-desc">Description</div><div class="slot-price"><span class="leader"></span><span class="s">S/$</span><span class="l">L/ $</span></div></div>
  <div class="slot" style="left:910px;top:765px"><div class="slot-name">Sushi Name</div><div class="slot-desc">Description</div><div class="slot-price"><span class="leader"></span><span class="s">S/$</span><span class="l">L/ $</span></div></div>
</main>
</body>
</html>
```